Real Estate Company
Tolin Estate Partners
Project: Real Estate Company
Real Estate Company - Real Estate
Creative Brief
Professional
Dale Moxon
Broker
PO Box 3152 Fresno, CA 93729
dale@tolinestatepartners.com
www.tolinestatepartners.com
BRE # 04527391
Card should have rounded edges.
one side of card should have all the info and one side should have logo + website

```html
<!DOCTYPE html>
<html lang="en">
<head>
<meta charset="utf-8">
<title>Tolin Estate Partners – Business Card</title>
<link rel="stylesheet" href="https://fonts.googleapis.com/css2?family=Arimo:wght@400;700&display=swap">
<style>
  :root {
    --backdrop: #5a5b5d;
    --card-white: #ffffff;
    --brand-blue: #1f6fb8;
    --logo-grey: #7d8389;
    --text-light: #ffffff;
    --web-ink: #0b3561;
  }
  * { box-sizing: border-box; margin: 0; padding: 0; }
  html, body { width: 1200px; height: 895px; overflow: hidden; }
  body {
    background: var(--backdrop);
    font-family: "Arimo", Arial, sans-serif;
    position: relative;
  }
  .card {
    position: absolute;
    width: 640px;
    height: 366px;
    border-radius: 18px;
    overflow: hidden;
    background: var(--card-white);
    box-shadow: 0 6px 18px rgba(0,0,0,0.35);
  }
  .card-front { left: 90px; top: 60px; }
  .card-back { left: 470px; top: 470px; }
  .card-art { position: absolute; inset: 0; width: 100%; height: 100%; }

  /* Front */
  .brand {
    position: absolute;
    left: 40px;
    top: 128px;
    width: 250px;
    display: flex;
    flex-direction: column;
    align-items: center;
    gap: 12px;
  }
  .brand-mark {
    width: 40px; height: 40px;
    background: var(--brand-blue);
  }
  .brand-name {
    font-size: 15px;
    font-weight: 700;
    letter-spacing: 1.5px;
    color: var(--logo-grey);
    text-transform: uppercase;
    white-space: nowrap;
  }
  .details {
    position: absolute;
    right: 30px;
    top: 34px;
    text-align: right;
    color: var(--text-light);
  }
  .person-name {
    font-size: 19px;
    font-weight: 400;
    letter-spacing: 0.5px;
    text-transform: uppercase;
  }
  .person-title { font-size: 13px; margin-top: 3px; }
  .licence { font-size: 12px; margin-top: 3px; }
  .address { font-size: 13px; line-height: 1.4; margin-top: 26px; }
  .contact-list { list-style: none; margin-top: 22px; }
  .contact-list li {
    display: flex;
    justify-content: flex-end;
    align-items: center;
    gap: 8px;
    font-size: 12px;
    line-height: 1;
    margin-bottom: 12px;
  }
  .contact-list li:nth-child(3) { margin-bottom: 20px; }
  .icon { width: 12px; height: 12px; flex: none; }

  /* Back */
  .website {
    position: absolute;
    left: 0; right: 0;
    bottom: 38px;
    text-align: center;
    font-size: 17px;
    letter-spacing: 6px;
    color: var(--web-ink);
  }
</style>
</head>
<body>

<section class="card card-front" aria-label="Card front">
  <svg class="card-art" viewBox="0 0 640 366" preserveAspectRatio="none" aria-hidden="true">
    <defs>
      <linearGradient id="frontBlue" x1="0" y1="0" x2="1" y2="1">
        <stop offset="0" stop-color="#3a95d8"/>
        <stop offset="0.55" stop-color="#1f6fb8"/>
        <stop offset="1" stop-color="#0f4f93"/>
      </linearGradient>
      <linearGradient id="frontPaper" x1="0" y1="0" x2="1" y2="0">
        <stop offset="0" stop-color="#ffffff"/>
        <stop offset="1" stop-color="#e9ecef"/>
      </linearGradient>
    </defs>
    <rect width="640" height="366" fill="url(#frontPaper)"/>
    <path d="M300 0 C385 60 395 300 330 366 L640 366 L640 0 Z" fill="#c9ced3"/>
    <path d="M314 0 C399 60 409 300 344 366 L640 366 L640 0 Z" fill="url(#frontBlue)"/>
  </svg>

  <div class="brand">
    <span class="brand-mark"></span>
    <span class="brand-name">Tolin Estate Partners</span>
  </div>

  <div class="details">
    <p class="person-name">Dale Moxon</p>
    <p class="person-title">Broker</p>
    <p class="licence">BRE # 04527391</p>
    <p class="address">PO Box 3152<br>Fresno, CA 93729</p>
    <ul class="contact-list">
      <li>559 214 8830
        <svg class="icon" viewBox="0 0 12 12" aria-hidden="true"><path d="M2.5 1 L4.5 1 L5 3.5 L3.8 4.5 Q5 7 7.5 8.2 L8.5 7 L11 7.5 L11 9.5 Q10.5 11 9 11 Q1 10 1 3 Q1 1.5 2.5 1 Z" fill="#fff"/></svg>
      </li>
      <li>559 214 8831
        <svg class="icon" viewBox="0 0 12 12" aria-hidden="true"><rect x="3" y="0.5" width="6" height="11" rx="1" fill="none" stroke="#fff" stroke-width="1.2"/><circle cx="6" cy="9.7" r="0.7" fill="#fff"/></svg>
      </li>
      <li>559 214 8832
        <svg class="icon" viewBox="0 0 12 12" aria-hidden="true"><rect x="3" y="1" width="6" height="4" fill="#fff"/><rect x="1" y="5" width="10" height="6" rx="1" fill="#fff"/></svg>
      </li>
      <li>dale@tolinestatepartners.com
        <svg class="icon" viewBox="0 0 12 12" aria-hidden="true"><rect x="1" y="2.5" width="10" height="7" fill="#fff"/><path d="M1 2.5 L6 6.5 L11 2.5" fill="none" stroke="#1f6fb8" stroke-width="1"/></svg>
      </li>
      <li>www.tolinestatepartners.com
        <svg class="icon" viewBox="0 0 12 12" aria-hidden="true"><circle cx="6" cy="6" r="5" fill="none" stroke="#fff" stroke-width="1.2"/><ellipse cx="6" cy="6" rx="2" ry="5" fill="none" stroke="#fff" stroke-width="1"/><line x1="1" y1="6" x2="11" y2="6" stroke="#fff" stroke-width="1"/></svg>
      </li>
    </ul>
  </div>
</section>

<section class="card card-back" aria-label="Card back">
  <svg class="card-art" viewBox="0 0 640 366" preserveAspectRatio="none" aria-hidden="true">
    <defs>
      <linearGradient id="backBlue" x1="0" y1="0" x2="1" y2="0">
        <stop offset="0" stop-color="#1f6fb8"/>
        <stop offset="0.5" stop-color="#3a95d8"/>
        <stop offset="1" stop-color="#0f4f93"/>
      </linearGradient>
    </defs>
    <rect width="640" height="366" fill="#ffffff"/>
    <path d="M0 170 C200 270 440 270 640 170 L640 366 L0 366 Z" fill="#c9ced3"/>
    <path d="M0 184 C200 284 440 284 640 184 L640 366 L0 366 Z" fill="url(#backBlue)"/>
  </svg>
  <p class="website">www.tolinestatepartners.com</p>
</section>

</body>
</html>
```